Finance Product Agency Business Card Design

We're an agency that provides products (service contracts, gap insurance, tire and wheel, etc) and support to dealership finance departments. We specialize in training finance producers to maximize their potential and also keep them up to date on the ever changing compliance and legal landscape. I'll attach an image of our logo, excited to see what you all come up with. Would also be interested in discussing our new website design with the winner.

Target Market(s)

auto dealerships

Industry/Entity Type

Business

Contact Information for Business Card

Mark Dolvery
Phone 317.624.5583
Fax 855.472.3308
email Mark.Dolvery@brightlanecoverage.example

Requirements
Must have
• basic contact information
Nice to have
• looking for something professional but modern

```html
<!DOCTYPE html>
<html lang="en">
<head>
<meta charset="utf-8">
<title>Brightlane Coverage – Business Card</title>
<link rel="stylesheet" href="https://fonts.googleapis.com/css2?family=Lato:wght@400;700;900&display=swap">
<style>
  :root {
    --page: #eceeef;
    --card: #ffffff;
    --ink: #2d3033;
    --charcoal: #25282b;
    --teal: #1f5f6e;
    --rule: #55595d;
    --soft-white: #e9eaeb;
  }
  * { box-sizing: border-box; margin: 0; padding: 0; }
  html, body { width: 1200px; height: 800px; overflow: hidden; }
  body {
    background: var(--page);
    font-family: "Lato", sans-serif;
    color: var(--ink);
    display: flex;
    flex-direction: column;
    align-items: center;
    justify-content: center;
    gap: 40px;
  }
  .card {
    position: relative;
    width: 560px;
    height: 320px;
    background: var(--card);
    box-shadow: 0 6px 18px rgba(0,0,0,0.12);
    overflow: hidden;
  }
  .brand-name {
    font-weight: 900;
    color: var(--ink);
    text-transform: uppercase;
    white-space: nowrap;
  }
  .brand-dot {
    flex: none;
    border-radius: 50%;
    background: var(--teal);
  }

  /* Front */
  .front-brand {
    position: absolute;
    left: 60px;
    top: 124px;
    display: flex;
    align-items: center;
    gap: 16px;
  }
  .front-brand .brand-dot { width: 52px; height: 52px; }
  .front-brand .brand-name { font-size: 30px; letter-spacing: 0.5px; }
  .front-rule {
    position: absolute;
    left: 60px; right: 40px;
    top: 200px;
    height: 1px;
    background: var(--rule);
  }

  /* Back */
  .back-shapes { position: absolute; inset: 0; }
  .back-brand {
    position: absolute;
    left: 30px; top: 36px;
    display: flex; align-items: center; gap: 10px;
  }
  .back-brand .brand-dot { width: 24px; height: 24px; }
  .back-brand .brand-name { font-size: 17px; letter-spacing: 0.5px; }
  .holder-name {
    position: absolute;
    right: 38px; top: 92px;
    text-align: right;
    color: #fff;
    font-weight: 900;
    font-size: 29px;
    line-height: 1.15;
    text-transform: uppercase;
  }
  .contact {
    position: absolute;
    color: var(--soft-white);
    font-size: 11.5px;
    letter-spacing: 0.2px;
    white-space: nowrap;
  }
  .contact-phone { right: 40px; top: 194px; text-align: right; line-height: 16px; }
  .contact-email { right: 40px; top: 280px; text-align: right; }
</style>
</head>
<body>

  <section class="card card-front" aria-label="Card front">
    <div class="front-brand">
      <span class="brand-dot"></span>
      <span class="brand-name">Brightlane Coverage</span>
    </div>
    <div class="front-rule"></div>
  </section>

  <section class="card card-back" aria-label="Card back">
    <svg class="back-shapes" width="560" height="320" viewBox="0 0 560 320">
      <polygon points="360,0 560,0 560,320 250,320 318,130" fill="var(--charcoal)"/>
      <polygon points="338,0 360,0 318,130 296,130" fill="var(--teal)"/>
      <polygon points="296,188 355,188 355,228 282,228" fill="var(--teal)"/>
      <polygon points="280,234 355,234 355,272 266,272" fill="var(--teal)"/>
      <line x1="355" y1="186" x2="525" y2="186" stroke="#4a4e52" stroke-width="1"/>
      <line x1="355" y1="231" x2="525" y2="231" stroke="#4a4e52" stroke-width="1"/>
      <line x1="355" y1="273" x2="525" y2="273" stroke="#4a4e52" stroke-width="1"/>
      <g fill="#fff" transform="translate(312,198)">
        <path d="M2 6 Q12 0 22 6 L20 10 L16 9 L15 6 Q12 5 9 6 L8 9 L4 10 Z"/>
        <rect x="5" y="11" width="14" height="9" rx="1.5"/>
        <circle cx="12" cy="15.5" r="2.2" fill="var(--teal)"/>
      </g>
      <g transform="translate(300,245)">
        <rect x="0" y="0" width="22" height="15" fill="#fff"/>
        <polyline points="0,0 11,8 22,0" fill="none" stroke="var(--teal)" stroke-width="1.5"/>
      </g>
    </svg>

    <div class="back-brand">
      <span class="brand-dot"></span>
      <span class="brand-name">Brightlane Coverage</span>
    </div>

    <h1 class="holder-name">Mark<br>Dolvery</h1>

    <p class="contact contact-phone">Phone: 317.624.5583<br>Fax: 855.472.3308</p>
    <p class="contact contact-email">Mark.Dolvery@brightlanecoverage.example</p>
  </section>

</body>
</html>
```